Copper Ridge Business Cards For New Startup

I am looking for you to design some business cards for a new startup https://copperridgehub.example. I have supplied logo, brand guidelines and our signatures as a guide.

We need this to reflect the brand guidelines and the website for brand consistency,

What is Copper Ridge?

Mallorca's Business Growth Community
Join your new business community full of passionate entrepreneurs who
love to solve problems and help each other grow together!

Any questions you can ask.

Target Market(s)

Business to Business

Contact Information for Business Card

These are attached (signatures) to the job

Font styles to use
Other font styles liked:
• Open Sans

Requirements
Must have
• Match design guidelines
Nice to have
• Photos of our faces so people remember us

```html
<!DOCTYPE html>
<html lang="en">
<head>
<meta charset="utf-8">
<title>Copper Ridge Business Card</title>
<link rel="stylesheet" href="https://fonts.googleapis.com/css2?family=Montserrat:wght@400;500;700;800&display=swap">
<style>
  :root {
    --backdrop: #2b2b2b;
    --brand: #5f5b1c;
    --brand-text: #6c6516;
    --card-white: #ffffff;
    --photo-tone: #c9ccd6;
    --photo-light: #eef0f4;
    --on-brand: #ffffff;
  }
  * { box-sizing: border-box; margin: 0; padding: 0; }
  html, body { width: 1200px; height: 900px; overflow: hidden; }
  body {
    background: var(--backdrop);
    font-family: "Montserrat", sans-serif;
    position: relative;
  }
  .card {
    position: absolute;
    top: 100px;
    width: 400px;
    height: 700px;
    box-shadow: 0 12px 30px rgba(0,0,0,.45);
  }
  .card-front {
    left: 170px;
    background: var(--brand);
    display: flex;
    align-items: center;
    justify-content: center;
    gap: 16px;
  }
  .brand-mark {
    width: 66px; height: 66px;
    border: 2px solid var(--on-brand);
    border-radius: 50%;
  }
  .brand-name {
    color: var(--on-brand);
    font-size: 30px;
    font-weight: 500;
    letter-spacing: .5px;
    text-transform: uppercase;
  }
  .card-back {
    left: 630px;
    background: var(--card-white);
    color: var(--brand-text);
    text-align: center;
  }
  .portrait {
    position: absolute;
    left: 0; top: 0;
    width: 100%; height: 340px;
    background:
      linear-gradient(to bottom, rgba(255,255,255,0) 60%, var(--card-white) 100%),
      radial-gradient(ellipse at 55% 70%, var(--photo-tone) 0%, var(--photo-light) 55%, var(--card-white) 90%);
  }
  .person-name {
    position: absolute;
    top: 380px; width: 100%;
    font-size: 27px;
    font-weight: 400;
    letter-spacing: .5px;
    text-transform: uppercase;
  }
  .person-name strong { font-weight: 800; }
  .person-role {
    position: absolute;
    top: 418px; width: 100%;
    font-size: 18px;
    font-weight: 500;
  }
  .contact-list {
    position: absolute;
    top: 478px; width: 100%;
    list-style: none;
    font-size: 19px;
    font-weight: 500;
    line-height: 32px;
  }
  .contact-list li { display: flex; justify-content: center; align-items: center; gap: 8px; }
  .contact-list svg { width: 18px; height: 18px; fill: var(--brand-text); }
  .social-row {
    position: absolute;
    top: 626px; left: 0; width: 100%;
    display: flex; align-items: center; justify-content: center; gap: 18px;
  }
  .social-row .rule { width: 62px; height: 2px; background: var(--brand-text); }
  .social-dot {
    width: 34px; height: 34px;
    border: 3px solid var(--brand-text);
    border-radius: 50%;
  }
</style>
</head>
<body>
  <section class="card card-front">
    <span class="brand-mark"></span>
    <span class="brand-name">Copper Ridge</span>
  </section>

  <section class="card card-back">
    <div class="portrait" role="img" aria-label="Head-and-shoulders portrait photo of the founder"></div>
    <h1 class="person-name"><strong>Daniel</strong> Reyes</h1>
    <p class="person-role">Founder &amp; Growth Hacker | Copper</p>
    <ul class="contact-list">
      <li>
        <svg viewBox="0 0 24 24" aria-hidden="true"><path d="M6.6 10.8a15 15 0 0 0 6.6 6.6l2.2-2.2c.3-.3.7-.4 1-.2 1.1.4 2.3.6 3.6.6.6 0 1 .4 1 1V20c0 .6-.4 1-1 1A17 17 0 0 1 3 4c0-.6.4-1 1-1h3.5c.6 0 1 .4 1 1 0 1.3.2 2.5.6 3.6.1.3 0 .7-.2 1z"/></svg>
        +34 600 000 123
      </li>
      <li>
        <svg viewBox="0 0 24 24" aria-hidden="true"><path d="M2 5h20v14H2z M3 6l9 7 9-7" fill="none" stroke="#6c6516" stroke-width="2"/></svg>
        dr@copperridgehub.example
      </li>
      <li>
        <svg viewBox="0 0 24 24" aria-hidden="true"><circle cx="12" cy="12" r="9" fill="none" stroke="#6c6516" stroke-width="2.5"/><circle cx="12" cy="12" r="4"/></svg>
        copperridgehub.example
      </li>
    </ul>
    <div class="social-row">
      <span class="rule"></span>
      <span class="social-dot"></span>
      <span class="social-dot"></span>
      <span class="social-dot"></span>
      <span class="social-dot"></span>
      <span class="social-dot"></span>
      <span class="rule"></span>
    </div>
  </section>
</body>
</html>
```